PDF Document Update

Hi,

I need the attached PDF document updated.

The word document attached outlines the new format for which I want the PDF to look like.

For the "Our People" section - please remove Orla Whitcombe and add in Brent Halloway (his photo is also attached).

Thanks!

```html
<!DOCTYPE html>
<html lang="en">
<head>
<meta charset="utf-8">
<title>KV Talent – Capability Statement</title>
<link href="https://fonts.googleapis.com/css2?family=Roboto+Condensed:wght@500;700&family=Roboto+Slab:wght@600&family=Hind:wght@300;400;500;600&display=swap" rel="stylesheet">
<style>
:root{
  --brand-blue:#233a93;
  --ink:#2a2a2e;
  --body:#3d3d42;
  --panel-grey:#ececee;
  --footer-grey:#58595b;
  --rule-grey:#9a9ba0;
  --backdrop:#2e2119;
  --white:#ffffff;
}
*{box-sizing:border-box;margin:0;padding:0}
html,body{width:1200px;height:1200px;overflow:hidden;background:var(--backdrop)}
.canvas{position:relative;width:1200px;height:1200px}
.page{position:absolute;top:238px;width:824px;height:1164px;background:var(--white);transform:scale(.6214);transform-origin:0 0;overflow:hidden;font-family:"Hind",sans-serif;color:var(--body)}
.page--overview{left:66px}
.page--people{left:621px}

/* hero */
.hero{position:absolute;left:0;top:0;width:824px;height:283px;background:#eef0f3}
.hero-photo{position:absolute;inset:0;clip-path:polygon(215px 0,824px 0,824px 283px,12px 283px);
  background:linear-gradient(180deg,#5d8fc9 0%,#9cc0e4 30%,#e9eef3 52%,#b9b7ae 62%,#4f86b0 72%,#2f6a9b 100%)}
.hero-corner{position:absolute;left:0;top:0}
.brand-name{position:absolute;right:40px;top:38px;font-family:"Hind",sans-serif;font-weight:500;color:var(--brand-blue);font-size:38px;line-height:38px;text-align:right;letter-spacing:1px}

.overview-panel{position:absolute;left:0;top:283px;width:824px;height:302px;background:var(--panel-grey);padding:14px 40px 0 39px}
.section-title{font-family:"Roboto Condensed",sans-serif;font-weight:700;color:var(--brand-blue);font-size:20px;line-height:22px;letter-spacing:.1px}
.section-title--mixed{font-weight:700;text-transform:none;margin-top:8px}
.copy{font-size:12.6px;line-height:16px;text-align:justify;margin-top:5px}
.services{display:grid;grid-template-columns:1fr 1fr 1fr;margin-top:8px}
.service{padding-right:12px;font-size:12.4px;line-height:15.8px;text-align:justify}
.service + .service{border-left:1px dotted var(--rule-grey);padding-left:11px}
.service-name{font-weight:600;color:var(--ink);display:block}

.risk-section{position:absolute;left:0;top:600px;width:824px;padding:0 40px 0 39px}
.mandates{display:grid;grid-template-columns:397px 1fr;margin-top:6px;list-style:none}
.mandate{position:relative;padding-left:16px;font-size:12.4px;line-height:18px;color:var(--body)}
.mandate::before{content:"";position:absolute;left:1px;top:4px;width:10px;height:10px;border-radius:50%;background:var(--brand-blue)}
.mandate::after{content:"";position:absolute;left:4.4px;top:6px;width:2.5px;height:4.5px;border:solid var(--white);border-width:0 1.3px 1.3px 0;transform:rotate(45deg)}

/* footer */
.footer{position:absolute;left:0;bottom:0;width:824px;height:52px}
.footer svg{position:absolute;inset:0}
.footer-item{position:absolute;top:0;height:48px;display:flex;align-items:center;gap:6px;color:var(--white);font-family:"Hind",sans-serif;font-size:14.5px;line-height:17px}
.footer-item svg{position:static;flex:none}

/* people */
.people-tab{position:absolute;left:40px;top:32px}
.people-tab-label{position:absolute;left:49px;top:33px;font-family:"Roboto Condensed",sans-serif;font-weight:700;font-size:24px;color:var(--white);letter-spacing:.3px}
.person{position:absolute;left:40px;width:745px;font-size:11.4px;line-height:15px;color:var(--body);text-align:justify}
.portrait{float:left;width:132px;height:132px;margin:-4px 8px 2px -4px;border-radius:50%;shape-outside:circle(50%);border:3px solid var(--brand-blue);box-shadow:inset 0 0 0 4px var(--white);
  background:radial-gradient(circle at 50% 40%,#d6b39d 0 16%,transparent 17%),linear-gradient(180deg,#56704a 0%,#3f5a3a 55%,#2b3a5e 56%,#1f2c4a 100%)}
.person-name{font-family:"Roboto Slab",serif;font-weight:600;color:var(--brand-blue);font-size:19px;line-height:21px;padding-top:2px}
.person-role{font-family:"Hind",sans-serif;font-weight:500;color:var(--ink);font-size:16px;line-height:18px;margin-bottom:2px}
.person-role--muted{font-weight:400;color:#55565c}
.person p{margin-bottom:4px}
</style>
</head>
<body>
<div class="canvas">

  <!-- Page one: overview -->
  <section class="page page--overview">
    <div class="hero">
      <div class="hero-photo" role="img" aria-label="Photo of a harbour city skyline with an opera house on the waterfront under a blue sky"></div>
      <svg class="hero-corner" width="230" height="283" viewBox="0 0 230 283">
        <polygon points="0,0 212,0 178,40 0,40" fill="#233a93"/>
        <line x1="215" y1="0" x2="12" y2="283" stroke="#ffffff" stroke-width="6"/>
      </svg>
      <div class="brand-name">KV<br>TALENT</div>
    </div>

    <div class="overview-panel">
      <h2 class="section-title">KV TALENT - CORPORATE OVERVIEW</h2>
      <p class="copy">KV Talent is an Australian recruitment firm and trusted recruitment partner to financial services firms, blue-chip corporates and professional services practices across Asia Pacific.</p>
      <p class="copy" style="margin-top:7px">We add value by leveraging our deep understanding of the industries, markets and disciplines that we serve, enabling us to present an informed and honest approach when providing recruitment advice. We remain focused on the belief that in any recruitment process diligence, honesty and integrity will always ensure the best outcome.</p>
      <h2 class="section-title section-title--mixed">KV Talent provides recruitment services that include :</h2>
      <div class="services">
        <div class="service"><span class="service-name">CONTINGENT RECRUITMENT -</span>Generally most suitable for team member level hiring, where utilising our extensive database and networking skills will provide a swift outcome.</div>
        <div class="service"><span class="service-name">EXECUTIVE SEARCH -</span>Most suitable for specialised and/or senior leadership positions. This service is a collaborative approach that includes comprehensive market mapping which provides a high level of assurance that the best candidate in the market is selected.</div>
        <div class="service"><span class="service-name">MARKET RESEARCH -</span>KV Talent provides ancillary research services including competitor analysis, candidate pool research and salary data. This service is highly valuable when employers are in the initial planning and scoping stage prior to undertaking a recruitment campaign.</div>
      </div>
    </div>

    <div class="risk-section">
      <h2 class="section-title">RISK MANAGEMENT, COMPLIANCE AND LEGAL RECRUITMENT</h2>
      <p class="copy">KV Talent has specialised in the risk management, compliance and legal recruitment market for 11 years. We partner with leading Australian and global corporations in the pursuit of talented employees within this rapidly changing field.</p>
      <p class="copy" style="margin-top:6px">Since inception, KV Talent has completed over 500 recruitment assignments within the risk, compliance and legal area, completing over 100 successful recruitment campaigns in the last 12 months.</p>
      <p class="copy" style="margin-top:6px">Our team of experienced consultants have deep knowledge of the dynamics of the candidate market along with the tools to be able to source candidates within this highly competitive recruitment field.</p>
      <p class="copy" style="margin-top:6px">Please see below for the a list of recently completed recruitment assignments, followed by the profiles of the members of the KV Talent Risk, Compliance and Legal recruitment team.</p>
      <h2 class="section-title" style="margin-top:12px">SELECTION OF RECENTLY COMPLETED MANDATES (2021/22)</h2>
      <ul class="mandates">
        <li class="mandate">Head of Compliance - Global Bank</li>
        <li class="mandate">Legal &amp; Compliance Officer - Global Asset Manager</li>
        <li class="mandate">Director - Legal &amp; Compliance - Global Fund</li>
        <li class="mandate">Control Room Compliance Manager - Aust. Bank</li>
        <li class="mandate">Director - Internal Audit - Leading Australian Bank</li>
        <li class="mandate">Credit Risk Manager - Global Bank</li>
        <li class="mandate">VP - IBD Compliance - Global Bank</li>
        <li class="mandate">Legal Counsel - Global Bank</li>
        <li class="mandate">Director - Compliance Consulting - Global Firm</li>
        <li class="mandate">Manager - Wealth Management Compliance</li>
        <li class="mandate">Director - Wealth Management Compliance Remediation</li>
        <li class="mandate">Compliance Manager - Global Bank - New Zealand</li>
        <li class="mandate">Head of Client Onboarding - Global Bank</li>
        <li class="mandate">Compliance Manager - Stockbroking</li>
        <li class="mandate">Director - Control Room - Australian Bank</li>
        <li class="mandate">Legal &amp; Compliance Manager - Aust. Fund Manager</li>
        <li class="mandate">Internal Audit Director - Leading Australian Bank</li>
        <li class="mandate">Associate - Wealth Management Compliance</li>
        <li class="mandate">Senior Manager - Technology Audit - Australian Bank</li>
        <li class="mandate">Senior Portfolio Risk Analyst - Global Bank</li>
        <li class="mandate">Senior Manager - Internal Audit - Australian Bank</li>
        <li class="mandate">Internal Audit Manager - Australian Bank</li>
        <li class="mandate">Associate Director - Compliance - Global Bank</li>
        <li class="mandate">Legal Counsel - Global Bank</li>
        <li class="mandate">Manager - Internal Audit - Leading Australian Bank</li>
        <li class="mandate">Compliance Officer - Australian Stockbroking</li>
        <li class="mandate">Manager - Compliance - Global Consulting Firm</li>
        <li class="mandate">Associate - Compliance Consulting - Global Firm</li>
        <li class="mandate">Compliance Manager - Retail Banking - Global Bank</li>
        <li class="mandate">AML/KYC Officer - Global Bank</li>
        <li class="mandate">Manager - Compliance Consulting - Global Firm</li>
        <li class="mandate">Legal &amp; Compliance Manager - Global Investment Bank</li>
      </ul>
    </div>

    <footer class="footer">
      <svg width="824" height="52" viewBox="0 0 824 52">
        <rect x="0" y="0" width="824" height="48" fill="#58595b"/>
        <rect x="0" y="48" width="824" height="4" fill="#233a93"/>
        <polygon points="0,0 200,0 222,52 0,52" fill="#233a93" stroke="#ffffff" stroke-width="3"/>
      </svg>
      <div class="footer-item" style="left:40px">
        <svg width="17" height="17" viewBox="0 0 17 17"><circle cx="8.5" cy="8.5" r="7.5" fill="none" stroke="#fff" stroke-width="1.2"/><path d="M8.5 4a2.6 2.6 0 0 0-2.6 2.6c0 2 2.6 5 2.6 5s2.6-3 2.6-5A2.6 2.6 0 0 0 8.5 4z" fill="#fff"/></svg>
        <span>1204/62 Marlow St,<br>&nbsp;Sydney, NSW, 2000</span>
      </div>
      <div class="footer-item" style="left:233px">
        <svg width="17" height="17" viewBox="0 0 17 17"><circle cx="8.5" cy="8.5" r="7.5" fill="none" stroke="#fff" stroke-width="1.2"/><path d="M5.5 4.8l1.6-.4 1 2-1 .8c.5 1.1 1.2 1.8 2.3 2.3l.8-1 2 1-.4 1.6c-3.4.1-6.4-2.9-6.3-6.3z" fill="#fff"/></svg>
        <span>+61 (0)2 5550 1287</span>
      </div>
      <div class="footer-item" style="left:407px">
        <svg width="17" height="17" viewBox="0 0 17 17"><circle cx="8.5" cy="8.5" r="7.5" fill="none" stroke="#fff" stroke-width="1.2"/><rect x="4.6" y="5.8" width="7.8" height="5.4" fill="#fff"/><path d="M4.6 5.8l3.9 3 3.9-3" fill="none" stroke="#58595b" stroke-width=".9"/></svg>
        <span>info@kvtalent.com.au</span>
      </div>
      <div class="footer-item" style="left:610px">
        <svg width="17" height="17" viewBox="0 0 17 17"><circle cx="8.5" cy="8.5" r="7.5" fill="none" stroke="#fff" stroke-width="1.2"/><circle cx="8.5" cy="8.5" r="4.2" fill="none" stroke="#fff" stroke-width="1"/><ellipse cx="8.5" cy="8.5" rx="1.8" ry="4.2" fill="none" stroke="#fff" stroke-width="1"/><line x1="4.3" y1="8.5" x2="12.7" y2="8.5" stroke="#fff" stroke-width="1"/></svg>
        <span>www.kvtalent.com.au</span>
      </div>
    </footer>
  </section>

  <!-- Page two: people -->
  <section class="page page--people">
    <svg class="people-tab" width="745" height="34" viewBox="0 0 745 34">
      <polygon points="0,0 176,0 188,30 0,30" fill="#233a93"/>
      <polygon points="180,0 186,0 198,30 192,30" fill="#233a93"/>
      <line x1="192" y1="31" x2="745" y2="31" stroke="#8a8b90" stroke-width="1.2"/>
    </svg>
    <div class="people-tab-label">OUR PEOPLE</div>

    <article class="person" style="top:78px">
      <div class="portrait" role="img" aria-label="Portrait photo of Callum Pryor"></div>
      <h3 class="person-name">CALLUM PRYOR</h3>
      <div class="person-role">Director/Founder</div>
      <p>Callum has 20+ years of financial services recruitment experience, with the past 19 years assisting clients across Asia Pacific with appointing senior infrastructure/middle office staff.</p>
      <p>After graduating from Eastport University in Australia with a degree in Environmental Science, Callum spent two years in London providing recruitment services to investment banks &amp; fund managers across a broad range of finance disciplines.</p>
      <p>In 2003 Callum returned to Sydney to focus on financial services recruitment within the Asia Pacific region, &amp; managing a multi-discipline recruitment division covering recruitment into risk, compliance, law, sales, marketing &amp; corporate advisory.</p>
      <p>Callum founded KV Talent in 2011 as a result of client demand for a senior specialist recruitment firm with deep experience in technical markets. His recruitment strategy has involved partnering with high profile Australian &amp; international financial services organisations, &amp; running bespoke recruitment campaigns to identify technical skill sets &amp; high performing professionals from manager to MD level appointments.</p>
      <p>Callum specialises in recruitment across the disciplines of: Compliance, operational risk, market risk, credit risk, internal audit, and law.</p>
    </article>

    <article class="person" style="top:300px">
      <div class="portrait" role="img" aria-label="Portrait photo of Duncan Ferris"></div>
      <h3 class="person-name">DUNCAN FERRIS</h3>
      <div class="person-role">Director</div>
      <p>Duncan has extensive experience in both executive search and contingent placement within the APAC region. After graduating from Southcoast University with a Bachelor of Commerce, Duncan spent four years in executive search, consulting within the fixed income trading arena, where he specialised in interest rate derivative and credit derivative trading in the Asia Pacific region.</p>
      <p>Having successfully developed and maintained a significant number of high quality relationships within the investment banking industry, Duncan went on to lead a team of recruitment consultants servicing the requirements of investment banks, corporate and retail banks, fund managers and other financial service providers.</p>
      <p>As a proven leader and well-connected executive search professional, Duncan has an excellent reputation in attaining results across a wide variety of assignments.</p>
    </article>

    <article class="person" style="top:498px">
      <div class="portrait" role="img" aria-label="Portrait photo of Marcus Tilden"></div>
      <h3 class="person-name">MARCUS TILDEN</h3>
      <div class="person-role">Director</div>
      <p>Marcus completed a Mathematics degree from Midlands University in the UK &amp; has over 10 years of executive search &amp; recruitment experience specialising in the financial services &amp; legal sectors across Asia Pacific &amp; the United States.</p>
      <p>Marcus commenced his career as a risk management specialist with two large European banks in London. Following this Marcus spent 7 years leading risk, compliance and legal recruitment teams in Sydney. Recently Marcus was the Head of the New York office for a large global recruitment firm, driving the US recruitment strategy across the disciplines of legal, compliance and technology.</p>
      <p>Marcus brings deep expertise in both the legal &amp; financial services industry along with the recruitment of high calibre professionals for technical roles.</p>
    </article>

    <article class="person" style="top:668px">
      <div class="portrait" role="img" aria-label="Portrait photo of Elliot Crane"></div>
      <h3 class="person-name">ELLIOT CRANE</h3>
      <div class="person-role">Principle</div>
      <p>Elliot Joined KV Talent in 2018, &amp; currently operates as a Principle within the Governance, Risk &amp; Compliance division of KV Talent. Elliot's role is focussed on assisting clients through the provision of bespoke services such as targeted headhunting &amp; market mapping. Elliot graduated with a degree in Sports &amp; Exercise Science from Goldbay University, QLD.</p>
      <p>Elliot is trained in executive search, headhunting &amp; market mapping, he assists clients with critical support in identifying &amp; sourcing talent, along with valuable advice on relevant industry trends, recruitment strategy &amp; market intelligence.</p>
    </article>

    <article class="person" style="top:806px">
      <div class="portrait" role="img" aria-label="Portrait photo of Harriet Vale"></div>
      <h3 class="person-name">HARRIET VALE</h3>
      <div class="person-role">Principle</div>
      <p>Hattie is a Principle operating within our Governance, Risk and Compliance recruitment practice. Hattie joined KV Talent after several years of professional experience gained in corporate law with a leading global law firm followed by a senior strategy position with a global retailer.</p>
      <p>Hattie has completed a significant number of high profile recruitment assignments in Australia from Analyst level appointments to Head of Legal, Company Secretary and Head of Compliance positions. Hattie is highly knowledgable on market supply &amp; demand dynamics, along with skilled in managing complex &amp; sensitive senior recruitment processes.</p>
      <p>Harriet has a degree in Arts/Laws from Capital Hill University.</p>
    </article>

    <article class="person" style="top:976px">
      <div class="portrait" role="img" aria-label="Portrait photo of Brent Halloway"></div>
      <h3 class="person-name">BRENT HALLOWAY</h3>
      <div class="person-role person-role--muted">Research Associate</div>
      <p>Brent competed a Bachelor of Business, Management and Marketing from Riverina Plains University. His role focusses on providing research assistance to our senior consultants when undertaking search assignments. This includes market mapping, headhunting and industry research campaigns.</p>
    </article>

    <footer class="footer">
      <svg width="824" height="52" viewBox="0 0 824 52">
        <rect x="0" y="0" width="824" height="48" fill="#58595b"/>
        <rect x="0" y="48" width="824" height="4" fill="#233a93"/>
        <polygon points="0,0 200,0 222,52 0,52" fill="#233a93" stroke="#ffffff" stroke-width="3"/>
      </svg>
      <div class="footer-item" style="left:40px">
        <svg width="17" height="17" viewBox="0 0 17 17"><circle cx="8.5" cy="8.5" r="7.5" fill="none" stroke="#fff" stroke-width="1.2"/><path d="M8.5 4a2.6 2.6 0 0 0-2.6 2.6c0 2 2.6 5 2.6 5s2.6-3 2.6-5A2.6 2.6 0 0 0 8.5 4z" fill="#fff"/></svg>
        <span>1204/62 Marlow St,<br>&nbsp;Sydney, NSW, 2000</span>
      </div>
      <div class="footer-item" style="left:233px">
        <svg width="17" height="17" viewBox="0 0 17 17"><circle cx="8.5" cy="8.5" r="7.5" fill="none" stroke="#fff" stroke-width="1.2"/><path d="M5.5 4.8l1.6-.4 1 2-1 .8c.5 1.1 1.2 1.8 2.3 2.3l.8-1 2 1-.4 1.6c-3.4.1-6.4-2.9-6.3-6.3z" fill="#fff"/></svg>
        <span>+61 (0)2 5550 1287</span>
      </div>
      <div class="footer-item" style="left:407px">
        <svg width="17" height="17" viewBox="0 0 17 17"><circle cx="8.5" cy="8.5" r="7.5" fill="none" stroke="#fff" stroke-width="1.2"/><rect x="4.6" y="5.8" width="7.8" height="5.4" fill="#fff"/><path d="M4.6 5.8l3.9 3 3.9-3" fill="none" stroke="#58595b" stroke-width=".9"/></svg>
        <span>info@kvtalent.com.au</span>
      </div>
      <div class="footer-item" style="left:610px">
        <svg width="17" height="17" viewBox="0 0 17 17"><circle cx="8.5" cy="8.5" r="7.5" fill="none" stroke="#fff" stroke-width="1.2"/><circle cx="8.5" cy="8.5" r="4.2" fill="none" stroke="#fff" stroke-width="1"/><ellipse cx="8.5" cy="8.5" rx="1.8" ry="4.2" fill="none" stroke="#fff" stroke-width="1"/><line x1="4.3" y1="8.5" x2="12.7" y2="8.5" stroke="#fff" stroke-width="1"/></svg>
        <span>www.kvtalent.com.au</span>
      </div>
    </footer>
  </section>

</div>
</body>
</html>
```